Redfern Espresso Branding
Business Cards & Stationary Set
Professional
Dale Ostrander
Manager
1875 Heron Ridge Ave.
Cedar Hollow, MN. 55987
r_fern@quillpost.net
I would like rounded corners on the business cards
Drive-thru to receive one free 12 oz. drink of choice!

```html
<!DOCTYPE html>
<html lang="en">
<head>
<meta charset="utf-8">
<title>Redfern Espresso – Business Card</title>
<link rel="stylesheet" href="https://fonts.googleapis.com/css2?family=Source+Sans+3:wght@400;600;700&display=swap">
<style>
  :root {
    --backdrop: #ece8e1;
    --card: #ffffff;
    --olive: #4f5a44;
    --rust: #c8642a;
    --ink: #2b2b2b;
    --muted: #6a6a6a;
  }
  * { margin: 0; padding: 0; box-sizing: border-box; }
  html, body {
    width: 1200px;
    height: 775px;
    overflow: hidden;
    background: var(--backdrop);
    font-family: "Source Sans 3", "Helvetica Neue", Arial, sans-serif;
  }
  .business-card {
    position: absolute;
    left: 40px;
    top: 67px;
    width: 1120px;
    height: 640px;
    background: var(--card);
    border-radius: 44px;
    overflow: hidden;
    box-shadow: 0 6px 18px rgba(0,0,0,0.18);
  }
  .edge-band {
    position: absolute;
    inset: 0;
    width: 100%;
    height: 100%;
  }
  .brand-mark {
    position: absolute;
    left: 174px;
    top: 118px;
    width: 324px;
    height: 383px;
    display: flex;
    flex-direction: column;
    align-items: center;
    justify-content: center;
    gap: 34px;
  }
  .brand-square {
    width: 150px;
    height: 150px;
    background: var(--olive);
  }
  .brand-name {
    color: var(--olive);
    font-weight: 700;
    font-size: 46px;
    line-height: 1.05;
    text-align: center;
    text-transform: uppercase;
    letter-spacing: 1px;
  }
  .divider {
    position: absolute;
    left: 596px;
    top: 146px;
    width: 12px;
    height: 236px;
  }
  .contact {
    position: absolute;
    left: 663px;
    top: 92px;
    color: var(--ink);
  }
  .person-name {
    color: var(--rust);
    font-weight: 600;
    font-size: 42px;
    line-height: 1.1;
  }
  .person-role {
    color: var(--muted);
    font-weight: 700;
    font-size: 27px;
    line-height: 1.2;
  }
  .address {
    margin-top: 132px;
    font-size: 31px;
    line-height: 1.6;
  }
  .contact-lines {
    margin-top: 18px;
    font-size: 31px;
    line-height: 1.55;
  }
  .contact-line {
    display: flex;
    align-items: center;
    gap: 12px;
  }
  .contact-icon {
    width: 26px;
    height: 26px;
    flex: none;
    color: var(--rust);
  }
  .at-sign {
    color: var(--rust);
    font-weight: 600;
    width: 26px;
    text-align: center;
  }
</style>
</head>
<body>
  <div class="business-card">
    <svg class="edge-band" viewBox="0 0 1120 640" preserveAspectRatio="none" aria-hidden="true">
      <path d="M0 0 L56 0 C110 200 130 440 175 640 L0 640 Z" fill="var(--rust)"/>
      <path d="M0 0 L24 0 C80 200 100 440 140 640 L0 640 Z" fill="var(--olive)"/>
    </svg>

    <div class="brand-mark">
      <div class="brand-square"></div>
      <div class="brand-name">Redfern<br>Espresso</div>
    </div>

    <svg class="divider" viewBox="0 0 12 236" aria-hidden="true">
      <path d="M6 0 L9 118 L6 236 L3 118 Z" fill="var(--ink)"/>
    </svg>

    <div class="contact">
      <div class="person-name">Dale Ostrander</div>
      <div class="person-role">Manager</div>
      <div class="address">
        <div>1875 Heron Ridge Ave.</div>
        <div>Cedar Hollow, MN. 55987</div>
      </div>
      <div class="contact-lines">
        <div class="contact-line">
          <svg class="contact-icon" viewBox="0 0 24 24" aria-hidden="true">
            <path fill="currentColor" d="M6.6 10.8c1.4 2.8 3.8 5.1 6.6 6.6l2.2-2.2c.3-.3.7-.4 1-.2 1.1.4 2.3.6 3.6.6.6 0 1 .4 1 1V20c0 .6-.4 1-1 1C10.6 21 3 13.4 3 4c0-.6.4-1 1-1h3.5c.6 0 1 .4 1 1 0 1.3.2 2.5.6 3.6.1.3 0 .7-.2 1L6.6 10.8z"/>
          </svg>
          <span>(612) 555-0148</span>
        </div>
        <div class="contact-line">
          <span class="at-sign">@</span>
          <span>r_fern@quillpost.net</span>
        </div>
      </div>
    </div>
  </div>
</body>
</html>
```